KVR Inc Web Design

WHAT ARE WE DOING?
We are developing a new website look and feel for a new company called KVR Inc. This new look and feel should include colors, design elements, choice of photography and other imagery, fonts, and other user experience elements.

WHAT DO THEY DO?
KVR, Inc, makes tools for researchers who are studying protein-protein interactions. These molecules are the basic tools of biology, and serve as key targets for drug developers and disease researchers. The world of proteins is enormously complex, and companies like KVR provide researchers with critical tools that help them elucidate this world.

WHO ARE WE TALKING TO?
The target audience for this website are professional scientists working in university research or biopharma drug development. They are highly sophisticated consumers looking for key tools that will advance their research.

WHAT DO WE WANT THEM TO DO?
The site is an information resource for the customer exploring the tools that KVR sells and the scientific issues surrounding protein-protein interactions. They should be able to navigate easily to their content of choice, while the whole site should convey a professionalism that enhanced KVR’s credibility.

WHAT DOES THE KVR BRAND STAND FOR?
KVR stands for illumination. Proteins are challenging to study, and KVR exists to help shed light on their workings.

WHAT ARE THE KEY VALUES OF THE KVR BRAND?
Integrity. Innovation. Insight.

WHAT ARE THE EXECUTIONAL MANDITORIES?
The look and feel is completely up for grabs. Nothing is off the table.

WHAT ARE THE DELIVERABLES?
We need new designs for the following templates:
http://cms.orvadeltaworks.com/
http://cms.orvadeltaworks.com/products-and-services/instruments-3/bench-top-instruments/
http://cms.orvadeltaworks.com/category/lab-study/

```html
<!DOCTYPE html>
<html lang="en">
<head>
<meta charset="utf-8">
<title>KVR Inc</title>
<link rel="stylesheet" href="https://fonts.googleapis.com/css2?family=Open+Sans:wght@400;600;700&family=Questrial&display=swap">
<style>
  :root {
    --orange: #f9ab2e;
    --teal: #2a8aa5;
    --grey-text: #5e5e5e;
    --grey-dark: #6b6b6b;
    --footer-bg: #6f6f6f;
    --white: #ffffff;
    --search-bg: #8a8a8a;
  }
  * { box-sizing: border-box; margin: 0; padding: 0; }
  html, body { width: 1200px; height: 909px; overflow: hidden; background: var(--white); }
  body { position: relative; font-family: "Open Sans", Arial, sans-serif; color: var(--grey-text); }
  a { text-decoration: none; }

  .top-rule { position: absolute; left: 0; top: 0; width: 1200px; height: 3px; background: var(--orange); }

  .brand { position: absolute; left: 120px; top: 14px; font-family: "Questrial", Arial, sans-serif;
    font-size: 30px; letter-spacing: 6px; color: var(--grey-dark); line-height: 34px; }

  .main-nav { position: absolute; left: 0; top: 20px; width: 940px; height: 24px;
    font-weight: 600; font-size: 15px; letter-spacing: -0.3px; color: var(--grey-dark); line-height: 22px; }
  .main-nav a { position: absolute; top: 0; color: inherit; white-space: nowrap; }
  .main-nav a.is-active { color: var(--orange); }

  .search { position: absolute; left: 942px; top: 19px; width: 138px; height: 24px;
    background: var(--search-bg); border-radius: 2px; color: #e4e4e4; font-size: 13px;
    line-height: 24px; padding-left: 8px; }
  .search svg { position: absolute; right: 6px; top: 5px; }

  .hero { position: absolute; left: 121px; top: 60px; width: 958px; height: 506px;
    background: linear-gradient(100deg, #dfe3e6 0%, #eef0f1 30%, #e9e7e4 55%, #d6d3cf 75%, #5a5c5e 100%); }
  .hero-caption { position: absolute; left: 0; width: 100%; top: 380px; text-align: center;
    font-family: "Questrial", Arial, sans-serif; font-size: 18px; line-height: 23px; color: #6a6a6a; }
  .hero-dots { position: absolute; left: 452px; top: 457px; display: flex; gap: 4px; }
  .hero-dots span { width: 11px; height: 11px; border-radius: 50%; background: var(--white);
    border: 2px solid #cfcfcf; }
  .hero-dots span.is-current { background: var(--orange); border-color: #fff; box-shadow: 0 0 0 1px #cfcfcf; }
  .hero-shadow { position: absolute; left: 121px; top: 566px; width: 958px; height: 24px;
    background: radial-gradient(ellipse at top, rgba(0,0,0,0.12), rgba(0,0,0,0) 70%); }

  .feature { position: absolute; top: 600px; width: 290px; height: 220px; text-align: center; }
  .feature-icon { height: 42px; display: flex; justify-content: center; align-items: flex-end; }
  .feature h2 { margin-top: 10px; font-size: 21px; font-weight: 700; color: var(--grey-dark); line-height: 28px; }
  .feature p { margin-top: 9px; font-size: 13.5px; line-height: 19px; color: var(--grey-text); }
  .feature--accent h2 { color: var(--orange); }
  .button { position: absolute; left: 60px; top: 180px; width: 171px; height: 28px;
    background: var(--teal); color: var(--white); font-family: "Questrial", Arial, sans-serif;
    font-size: 16px; line-height: 28px; text-align: left; padding-left: 28px; white-space: nowrap; }
  .button--order { background: var(--orange); }
  .button--wide { padding-left: 20px; }
  .button svg { position: absolute; right: 16px; top: 8px; }

  .site-footer { position: absolute; left: 0; top: 847px; width: 1200px; height: 62px; background: var(--footer-bg); }
  .footer-nav { position: absolute; left: 121px; top: 24px; font-size: 13px; color: var(--white); }
  .footer-nav span.sep { margin: 0 6px; }
  .social { position: absolute; left: 824px; top: 21px; display: flex; gap: 6px; }
  .social span { width: 24px; height: 24px; border-radius: 50%; background: var(--white); }
  .copyright { position: absolute; left: 929px; top: 24px; font-size: 14px; color: var(--white); }
  .copyright em { font-style: normal; color: var(--orange); }
</style>
</head>
<body>
  <div class="top-rule"></div>
  <div class="brand">KVR INC</div>

  <nav class="main-nav">
    <a href="#" style="left:305px">Company</a>
    <a href="#" class="is-active" style="left:398px">Products &amp; Services</a>
    <a href="#" style="left:562px">Learning Center</a>
    <a href="#" style="left:700px">Events</a>
    <a href="#" style="left:771px">KVR News</a>
    <a href="#" style="left:862px">Contact</a>
  </nav>

  <div class="search">Search
    <svg width="14" height="14" viewBox="0 0 14 14"><circle cx="6" cy="6" r="4.5" fill="none" stroke="#d8d8d8" stroke-width="1.5"/><line x1="9.3" y1="9.3" x2="13" y2="13" stroke="#d8d8d8" stroke-width="2"/></svg>
  </div>

  <section class="hero" role="img" aria-label="Photo of a scientist in a lab coat and hair net looking into a microscope in a bright laboratory">
    <p class="hero-caption">What are the Implications of GPCR Heterotrimerization<br>for the Drug Discovery Process ? &nbsp;»</p>
    <div class="hero-dots"><span class="is-current"></span><span></span><span></span><span></span></div>
  </section>
  <div class="hero-shadow"></div>

  <section class="feature" style="left:113px">
    <div class="feature-icon">
      <svg width="28" height="42" viewBox="0 0 28 42"><rect x="10" y="1" width="8" height="3" fill="#6b6b6b"/><path d="M11 4 V16 L2 37 Q1 40 4 40 H24 Q27 40 26 37 L17 16 V4" fill="none" stroke="#6b6b6b" stroke-width="2.5"/><path d="M7 28 H21 L25 38 H3 Z" fill="#6b6b6b"/></svg>
    </div>
    <h2>Innovation</h2>
    <p>Lorem ipsum dolor sit amet, consectetur adipiscing elit. Proin placerat nulla massa, condimentum leo tincidunt vel. Consectetur adipiscing elit nulla.</p>
    <a class="button" href="#">Learn More<svg width="18" height="12" viewBox="0 0 18 12"><path d="M0 3 H9 V0 L18 6 L9 12 V9 H0 Z" fill="#fff"/></svg></a>
  </section>

  <section class="feature feature--accent" style="left:455px">
    <div class="feature-icon">
      <svg width="40" height="42" viewBox="0 0 40 42"><rect x="12" y="2" width="9" height="20" rx="2" transform="rotate(-30 16 12)" fill="#f9ab2e"/><circle cx="22" cy="22" r="7" fill="none" stroke="#f9ab2e" stroke-width="4"/><rect x="6" y="36" width="30" height="5" fill="#f9ab2e"/><path d="M28 22 Q34 30 26 36" fill="none" stroke="#f9ab2e" stroke-width="4"/></svg>
    </div>
    <h2>Automation</h2>
    <p>Lorem ipsum dolor sit amet, consectetur adipiscing elit. Proin placerat nulla massa, condimentum leo tincidunt vel. Consectetur adipiscing elit nulla .</p>
    <a class="button button--order" href="#">Order Today<svg width="18" height="12" viewBox="0 0 18 12"><path d="M0 3 H9 V0 L18 6 L9 12 V9 H0 Z" fill="#fff"/></svg></a>
  </section>

  <section class="feature" style="left:795px">
    <div class="feature-icon">
      <svg width="48" height="40" viewBox="0 0 48 40"><circle cx="22" cy="16" r="11" fill="none" stroke="#6b6b6b" stroke-width="4"/><line x1="14" y1="24" x2="3" y2="36" stroke="#6b6b6b" stroke-width="6" stroke-linecap="round"/><circle cx="22" cy="16" r="3" fill="#6b6b6b"/><circle cx="38" cy="20" r="3" fill="#6b6b6b"/><circle cx="44" cy="28" r="2.5" fill="#6b6b6b"/><circle cx="34" cy="32" r="2.5" fill="#6b6b6b"/><line x1="38" y1="20" x2="44" y2="28" stroke="#6b6b6b" stroke-width="1.5"/><line x1="38" y1="20" x2="34" y2="32" stroke="#6b6b6b" stroke-width="1.5"/></svg>
    </div>
    <h2>Research</h2>
    <p>Lorem ipsum dolor sit amet, consectetur adipiscing elit. Proin placerat nulla massa, condimentum leo tincidunt vel. Consectetur adipiscing elit nulla.</p>
    <a class="button button--wide" href="#">The Challenge<svg width="18" height="12" viewBox="0 0 18 12"><path d="M0 3 H9 V0 L18 6 L9 12 V9 H0 Z" fill="#fff"/></svg></a>
  </section>

  <footer class="site-footer">
    <div class="footer-nav">Company<span class="sep">-</span>Products &amp; Services<span class="sep">-</span>Learning Center<span class="sep">-</span>Events<span class="sep">-</span>KVR News<span class="sep">-</span>Contact</div>
    <div class="social"><span></span><span></span><span></span></div>
    <div class="copyright">Copyright © <em>KVR Inc.</em> 2013</div>
  </footer>
</body>
</html>
```